Design a Professional Business Card for Velmora Arcs

Design a business card for Velmora Arcs, we are a National Sport Court Company.

West Region Address: 4175 Quill Harbor Ln, Suite #215 Englewood, Colorado 80467
East Region Address: 3817 Tamsin Rd E, Bradenton, Florida 34583

Target Market(s)

High End Residential & Institutional Clients

Industry/Entity Type

Design & Construction

Contact Information for Business Card

Logo/Brand/Colors/ name, number (provided in comments)

Requirements
Must have
• Colors only provided in logo
Should not have
• Any other colors not in existing logo (attached)

```html
<!DOCTYPE html>
<html lang="en">
<head>
<meta charset="utf-8">
<title>Velmora Arcs Business Card</title>
<link href="https://fonts.googleapis.com/css2?family=Roboto:wght@400;500;700;900&display=swap" rel="stylesheet">
<style>
  :root {
    --navy: #1e3765;
    --green: #0b7134;
    --white: #ffffff;
    --ink: #2a2a2a;
    --stage: #e9ebee;
  }
  * { box-sizing: border-box; margin: 0; padding: 0; }
  html, body { width: 1200px; height: 900px; overflow: hidden; }
  body {
    background: var(--stage);
    font-family: "Roboto", Arial, sans-serif;
    display: flex;
    flex-direction: column;
    align-items: center;
    justify-content: center;
    gap: 36px;
  }
  .card {
    width: 700px;
    height: 400px;
    border-radius: 22px;
    position: relative;
    overflow: hidden;
    box-shadow: 0 6px 18px rgba(0,0,0,0.15);
  }
  .card-front {
    background: var(--navy);
    display: flex;
    align-items: center;
    justify-content: center;
  }
  .brand {
    display: flex;
    align-items: center;
    gap: 22px;
  }
  .brand-mark {
    border-radius: 50%;
    flex: none;
  }
  .brand-name {
    font-weight: 900;
    text-transform: uppercase;
    letter-spacing: 4px;
    line-height: 0.95;
  }
  .card-front .brand-mark { width: 120px; height: 120px; background: var(--green); }
  .card-front .brand-name { color: var(--white); font-size: 58px; }

  .card-back { background: var(--white); }
  .card-back .brand {
    position: absolute;
    left: 40px;
    top: 88px;
    gap: 14px;
  }
  .card-back .brand-mark { width: 72px; height: 72px; background: var(--green); }
  .card-back .brand-name { color: var(--navy); font-size: 38px; letter-spacing: 3px; }

  .divider {
    position: absolute;
    left: 362px;
    top: 36px;
    width: 2px;
    height: 150px;
    background: linear-gradient(var(--green), rgba(11,113,52,0.15));
  }
  .person {
    position: absolute;
    left: 392px;
    top: 30px;
  }
  .person-name { color: var(--navy); font-weight: 700; font-size: 27px; }
  .person-role { color: var(--ink); font-size: 15px; margin: 2px 0 14px 14px; }
  .contact-list { list-style: none; }
  .contact-list li {
    display: flex;
    align-items: center;
    gap: 12px;
    font-size: 15px;
    color: var(--ink);
    margin-bottom: 8px;
    padding-left: 14px;
  }
  .contact-list svg { width: 16px; height: 16px; flex: none; fill: var(--green); }

  .address {
    position: absolute;
    text-align: center;
    color: var(--ink);
    font-size: 15px;
    line-height: 1.35;
  }
  .address svg { width: 16px; height: 20px; fill: var(--green); display: block; margin: 0 auto 8px; }
  .address-east { right: 40px; top: 205px; width: 260px; }
  .address-west { left: 130px; top: 250px; width: 300px; }

  .edge-band {
    position: absolute;
    left: 0; right: 0; bottom: 0;
    height: 10px;
  }
</style>
</head>
<body>
  <section class="card card-front">
    <div class="brand">
      <span class="brand-mark"></span>
      <span class="brand-name">Velmora<br>Arcs</span>
    </div>
  </section>

  <section class="card card-back">
    <div class="brand">
      <span class="brand-mark"></span>
      <span class="brand-name">Velmora<br>Arcs</span>
    </div>

    <div class="divider"></div>

    <div class="person">
      <p class="person-name">Darren Okafor</p>
      <p class="person-role">Owner</p>
      <ul class="contact-list">
        <li>
          <svg viewBox="0 0 24 24"><path d="M6.6 10.8a15 15 0 0 0 6.6 6.6l2.2-2.2a1 1 0 0 1 1-.25 11.4 11.4 0 0 0 3.6.57 1 1 0 0 1 1 1V20a1 1 0 0 1-1 1A17 17 0 0 1 3 4a1 1 0 0 1 1-1h3.5a1 1 0 0 1 1 1c0 1.25.2 2.45.57 3.57a1 1 0 0 1-.25 1z"/></svg>
          (407) 555-0184
        </li>
        <li>
          <svg viewBox="0 0 24 24"><path d="M2 5h20v14H2z M2 5l10 8 10-8" /></svg>
          hello@velmoraarcs.com
        </li>
        <li>
          <svg viewBox="0 0 24 24"><circle cx="12" cy="12" r="10"/></svg>
          www.velmoraarcs.com
        </li>
      </ul>
    </div>

    <div class="address address-east">
      <svg viewBox="0 0 16 20"><path d="M8 0a8 8 0 0 0-8 8c0 6 8 12 8 12s8-6 8-12a8 8 0 0 0-8-8zm0 11a3 3 0 1 1 0-6 3 3 0 0 1 0 6z"/></svg>
      East Region Address:<br>
      3817 Tamsin Rd E, Bradenton,<br>
      Florida 34583
    </div>

    <div class="address address-west">
      <svg viewBox="0 0 16 20"><path d="M8 0a8 8 0 0 0-8 8c0 6 8 12 8 12s8-6 8-12a8 8 0 0 0-8-8zm0 11a3 3 0 1 1 0-6 3 3 0 0 1 0 6z"/></svg>
      West Region Address:<br>
      4175 Quill Harbor Ln, Suite<br>
      #215 Englewood, Colorado 80467
    </div>

    <svg class="edge-band" viewBox="0 0 700 10" preserveAspectRatio="none">
      <polygon points="0,10 0,6 500,0 700,0 700,10" fill="var(--green)"/>
      <polygon points="500,0 700,0 700,10 490,10" fill="var(--navy)"/>
    </svg>
  </section>
</body>
</html>
```